Header/Logo Redesign

****WE HAVE FOUND THE DESIGNER WHO WILL BE HANDLING THIS PROJECT. PLEASE DONT SUBMIT ANY MORE DESIGNS.****
We have been working with a Web/Logo Designer on a new header and logo for our site. We like some of it, but other things need changing.
Overall Look: We are looking for something that is professional, yet still fresh. Most business two business websites seem old fashinoned. The site we like most is www.tallyhaven.com.
Header Thoughts:
-We like the color at the top of the header. The light purple on the menu bar is a little dull though. It seems to be grayed out too much. Notice the pop that www.tallyhaven.com has. We need that pop.
-The fonts on the menu bar don't pop either. I don't know if it is because the font is bad or the thickness of the font is bad or what.
-We are not sold on the green color in the logo and header. It is pretty good, but maybe we can test other colors?
Logo Thoughts:
-I am not sold on the green color. It is pretty good, but maybe test it out with some other colors?
-The logo does not pop like the www.tallyhaven.com logo pops.
-We had started thinking about doing an owl as part of our name/logo or maybe some other type of animal. Look at the ideas I had sent our original graphic designer.
A. http://markvista.net/gallery/detail/842907 - i like that is simple, a little abstract, but I don't like that it is sort of evil.
B. http://markvista.net/gallery/detail/27514 - i like that is abstract.
C. http://pixelbrook.files.quillsite.net/2012/05/torvane4.jpg - i like the slightly abstract.
D. http://sketchlark.net/shots/718204-O-W-L - good - abrstract and slightly turned.
Target Market(s)
Sales and Marketing People - primarily a masculine audience in their 20s to 40s.
Industry/Entity Type
Business
Look and feel

```html
<!DOCTYPE html>
<html lang="en">
<head>
<meta charset="utf-8">
<title>Scout 360 – Header</title>
<link rel="stylesheet" href="https://fonts.googleapis.com/css2?family=Nunito+Sans:wght@400;700;800&display=swap">
<style>
  :root {
    --band-line: #3f2270;
    --band-top: #55318a;
    --band-main: #4e2a80;
    --band-edge: #6c4c9c;
    --page: #ffffff;
    --nav-text: #c3bad0;
    --brand-text: #ffffff;
    --tab-bg: #ffffff;
    --tab-text: #555555;
    --tab-link: #4e2a80;
    --search-bg: #5c3a90;
    --search-divider: #4a2778;
    --search-text: #b9aecb;
    --accent: #8cc43f;
  }
  * { box-sizing: border-box; margin: 0; padding: 0; }
  html, body { width: 1200px; height: 207px; overflow: hidden; background: var(--page); }
  body { font-family: "Nunito Sans", sans-serif; position: relative; }

  .site-header { position: absolute; left: 0; top: 0; width: 1200px; height: 116px; }
  .band-line { position: absolute; left: 0; top: 0; width: 100%; height: 3px; background: var(--band-line); }
  .band-top { position: absolute; left: 0; top: 3px; width: 100%; height: 31px; background: var(--band-top); }
  .band-main { position: absolute; left: 0; top: 34px; width: 100%; height: 79px; background: var(--band-main); }
  .band-edge { position: absolute; left: 0; top: 113px; width: 100%; height: 3px; background: var(--band-edge); }

  .account-tab {
    position: absolute; left: 843px; top: 3px; width: 168px; height: 23px;
    background: var(--tab-bg); border-radius: 0 0 4px 4px;
    display: flex; align-items: center; justify-content: center; gap: 8px;
    font-size: 11px; color: var(--tab-text);
  }
  .account-tab .divider { width: 1px; height: 10px; border-left: 1px dotted #999; }
  .account-tab .signup { color: var(--tab-link); }

  .brand-mark {
    position: absolute; left: 204px; top: 42px; width: 56px; height: 56px;
    border: 3px solid var(--brand-text); border-radius: 4px;
  }
  .brand {
    position: absolute; left: 279px; top: 69px;
    font-size: 22px; font-weight: 800; letter-spacing: 1px;
    color: var(--brand-text); line-height: 26px; white-space: nowrap;
  }

  .main-nav {
    position: absolute; left: 452px; top: 76px;
    font-size: 11px; font-weight: 700; color: var(--nav-text); letter-spacing: .2px;
  }
  .main-nav a { color: inherit; text-decoration: none; position: absolute; white-space: nowrap; }

  .search {
    position: absolute; left: 844px; top: 69px; width: 167px; height: 28px;
    background: var(--search-bg); border-radius: 3px;
    display: flex; align-items: center;
  }
  .search .field { flex: 1; padding-left: 5px; font-size: 10px; color: var(--search-text); }
  .search .button { width: 26px; height: 100%; border-left: 1px solid var(--search-divider); display: flex; align-items: center; justify-content: center; }
</style>
</head>
<body>
  <header class="site-header">
    <div class="band-line"></div>
    <div class="band-top"></div>
    <div class="band-main"></div>
    <div class="band-edge"></div>

    <div class="account-tab">
      <span class="login">Account Login</span>
      <span class="divider"></span>
      <span class="signup">Free Sing Up</span>
    </div>

    <div class="brand-mark" aria-hidden="true"></div>
    <div class="brand">SCOUT 360</div>

    <nav class="main-nav">
      <a href="#" style="left:0">NEWS</a>
      <a href="#" style="left:64px">PEOPLE</a>
      <a href="#" style="left:135px">COMPANIES</a>
      <a href="#" style="left:229px">DOWNLOADS</a>
    </nav>

    <div class="search">
      <span class="field">Search</span>
      <span class="button">
        <svg width="13" height="13" viewBox="0 0 13 13" aria-hidden="true">
          <circle cx="5.5" cy="5.5" r="4" fill="none" stroke="var(--accent)" stroke-width="2"/>
          <line x1="8.5" y1="8.5" x2="12" y2="12" stroke="var(--accent)" stroke-width="2.2" stroke-linecap="round"/>
        </svg>
      </span>
    </div>
  </header>
</body>
</html>
```